Pamphlet Days of the Family - École Sainte-Ondine

We * need a pamphlet (flyer) to describe a new project. This project is called "Family Days - École Sainte-Ondine". The text describing family days and their intended goals is attached in the downloaded .doc document. We also provided the logo (LA PRIMOVEL no font in attachment) which represents the school and those days of the family. Please write "Family Days - École Sainte-Ondine" on top of the pamphlet with the Logo in plain view (The text The days of the École Sainte-Ondine family must be associated with the logo). We need the pamphlet to be colorful, attractive and clean as much as possible. We would like to have childish drawings (see drawing example attached) and photos that represent one or both parents with their child (ren) in a SCHOOL ENVIRONMENT (very important). Parents must feel concerned. It can be a two-sided pamphlet. In color (bright colors as much as possible). The text must be in French so only FRENCH DESIGNERS ARE INVITED to work on this design because the text must remain consistent. The project can be summed up as follows: The Sainte-Ondine School wishes to open its doors so that parents can share with their child moments in their student life. They will be invited, at various times of the school year, to participate in the daily life of their child, for example ... • during special activities in class (eg reading, do-it-yourself, job presentation, etc.). events (eg, back to school, Christmas choir, carnival, etc.) • during educational and sports outings (eg skating, library, cinema, etc.) Also, they will have the opportunity to come and spend a period in their child's classroom. They will have the privilege of accompanying him during a usual learning moment. For any additional question, thank you to contact me via this page, it will be my pleasure to answer you quickly. Thank you all for your participation. * We are a committee made up of parents, teachers, school principal, school administrators. Everyone has a say in the final design. So I am only the intermediary responsible for the project. It will be my pleasure to share with you the information received from these different partners for this project.

Target Market(s)

Parents of students at a primary school (ages 5 to 12).

Font styles to use
Sans Serif

Colors

Designer to choose colors to be used in the design.

Requirements
Must have
• The Logo prominently Pamphlet Colorful (beautiful bright colors) Easy to read and understand (some parents speak very little French) Originality (Attractive) Text In French (required) and consistent
Nice to have
• One or more Childish Drawing (s) One (1) parent-child Photo (s) in a school environment Allure Épuré
Should not have
• The Dark Colors Of the Scriptures Too Small A Condensed Text Text English

```html
<!DOCTYPE html>
<html lang="fr">
<head>
<meta charset="utf-8">
<title>Les journées de la famille de Sainte-Ondine</title>
<link href="https://fonts.googleapis.com/css2?family=Source+Sans+3:ital,wght@0,400;0,600;0,700;1,700;1,800&family=Arimo:wght@400;700&display=swap" rel="stylesheet">
<style>
  :root {
    --page-bg: #ecebe7;
    --yellow: #fcd232;
    --yellow-deep: #f6c21d;
    --orange: #f39a2d;
    --orange-red: #ef6f2a;
    --lime: #e3e230;
    --ink: #1d1d1b;
    --text: #2b2b2b;
    --navy: #1f2a4d;
    --white: #ffffff;
  }
  * { box-sizing: border-box; margin: 0; padding: 0; }
  html, body { width: 1200px; height: 900px; overflow: hidden; background: var(--page-bg); }
  body { position: relative; font-family: "Arimo", Arial, sans-serif; color: var(--text); }

  .spread {
    position: absolute; left: 71px; top: 50px; width: 1058px; height: 747px;
    background: var(--white); box-shadow: 0 2px 8px rgba(0,0,0,.12); overflow: hidden;
  }

  /* ---------- left panel ---------- */
  .goals-panel { position: absolute; left: 0; top: 0; width: 528px; height: 600px; background: var(--yellow); }
  .goals-panel::after { content: ""; position: absolute; left: 0; right: 0; bottom: -4px; height: 5px; background: var(--yellow-deep); }

  .connectors { position: absolute; left: 0; top: 0; width: 528px; height: 600px; }

  .goal-box {
    position: absolute; border: 2px solid var(--ink); border-radius: 22px; padding: 12px 18px 0 22px;
  }
  .goal-title { font-family: "Source Sans 3", sans-serif; font-style: italic; font-weight: 800; font-size: 17px; color: var(--ink); margin-bottom: 4px; }
  .goal-list { list-style: none; font-size: 12px; line-height: 15px; color: var(--text); }
  .goal-list li { position: relative; padding-left: 13px; }
  .goal-list li::before { content: "•"; position: absolute; left: 0; }

  .box-child { left: 43px; top: 42px; width: 420px; height: 117px; }
  .box-school { left: 16px; top: 208px; width: 370px; height: 178px; }
  .box-school .goal-title + .goal-list { margin-bottom: 12px; }
  .box-parent { left: 63px; top: 437px; width: 400px; height: 126px; padding-left: 24px; }

  .role-badge {
    position: absolute; width: 140px; height: 140px; border-radius: 50%; border: 2px solid var(--ink);
    background: var(--yellow); display: flex; align-items: center; justify-content: center;
  }
  .role-photo {
    width: 126px; height: 126px; border-radius: 50%; overflow: hidden; position: relative;
  }
  .role-label {
    position: absolute; left: 0; right: 0; font-family: "Source Sans 3", sans-serif; font-style: italic; font-weight: 700;
    color: var(--white); text-align: center; font-size: 16px; line-height: 18px;
  }
  .badge-child { left: 320px; top: 25px; }
  .badge-child .role-photo { background: linear-gradient(160deg, #cfd7e2 0%, #8c9bb4 55%, #3b4a6b 100%); }
  .badge-child .role-label { bottom: 24px; height: 26px; line-height: 26px; background: var(--navy); }
  .badge-school { left: 264px; top: 210px; }
  .badge-school .role-photo { background: linear-gradient(160deg, #c9d7e4 0%, #b14a3a 55%, #7e1d1f 100%); }
  .badge-school .role-label { top: 38px; padding: 4px 0; background: rgba(130,20,25,.85); }
  .badge-parent { left: 328px; top: 425px; }
  .badge-parent .role-photo { background: linear-gradient(180deg, #f3ecd5 0%, #c9b98c 45%, #4b5a2f 70%, #8aa64a 100%); }
  .badge-parent .role-label { bottom: 30px; height: 26px; line-height: 26px; background: rgba(40,50,30,.85); }

  .side-title {
    position: absolute; left: 433px; top: 195px; width: 200px; height: 44px;
    transform-origin: left top; transform: translate(0, 200px) rotate(-90deg) translate(-10px, 0);
    font-family: "Source Sans 3", sans-serif; font-style: italic; font-weight: 800; font-size: 15px; line-height: 17px;
    color: var(--ink); text-align: center;
  }

  .participation-note { position: absolute; left: 33px; top: 618px; width: 470px; font-size: 12px; line-height: 15px; color: var(--text); }
  .participation-note p + p { margin-top: 12px; }

  /* ---------- right panel ---------- */
  .cover-photo {
    position: absolute; left: 528px; top: 0; width: 530px; height: 300px;
    background: linear-gradient(135deg, #f2ead8 0%, #d9c9a8 35%, #c89b6e 60%, #e6c79a 80%, #9db86a 100%);
  }
  .photo-curve { position: absolute; left: 528px; top: 230px; width: 530px; height: 80px; }

  .kid-drawing { position: absolute; border: 5px solid var(--white); box-shadow: 0 2px 6px rgba(0,0,0,.25); }
  .drawing-left { left: 548px; top: 268px; width: 140px; height: 110px; transform: rotate(10deg);
    background: linear-gradient(160deg, #cfe9f4 0%, #f3d36a 40%, #7fc36a 75%, #4f9b48 100%); }
  .drawing-left-back { left: 543px; top: 330px; width: 145px; height: 80px; transform: rotate(-6deg);
    background: linear-gradient(160deg, #c7e3a8 0%, #6fb7d9 50%, #d87e6b 100%); }
  .drawing-right { left: 895px; top: 278px; width: 146px; height: 118px; transform: rotate(-10deg);
    background: linear-gradient(160deg, #ffffff 0%, #eaf4d9 35%, #8cc46a 65%, #5aa6c9 100%); }

  .logo-disc {
    position: absolute; left: 718px; top: 255px; width: 150px; height: 150px; border-radius: 50%;
    background: var(--white); display: flex; align-items: center; justify-content: center;
  }
  .logo-name { font-family: "Source Sans 3", sans-serif; font-weight: 700; font-size: 22px; color: var(--orange); }

  .event-title {
    position: absolute; left: 660px; top: 402px; width: 260px; text-align: center;
    font-family: "Source Sans 3", sans-serif; font-style: italic; font-weight: 800; font-size: 16px; line-height: 19px; color: var(--ink);
  }

  .intro-text { position: absolute; left: 560px; top: 460px; width: 463px; font-size: 12px; line-height: 15px; text-align: justify; color: var(--text); }
  .intro-text p + p { margin-top: 11px; }

  .occasion-row { position: absolute; left: 528px; top: 570px; width: 530px; height: 88px; display: flex; }
  .occasion {
    flex: 1; display: flex; align-items: center; justify-content: center; text-align: center;
    font-family: "Source Sans 3", sans-serif; font-style: italic; font-weight: 700; font-size: 10.5px; line-height: 13px; color: var(--ink);
  }
  .occasion-class { background: var(--yellow); }
  .occasion-events { background: linear-gradient(135deg, var(--orange-red) 0%, var(--orange) 55%, #f7c13a 100%); }
  .occasion-outings { background: linear-gradient(135deg, var(--lime) 0%, var(--yellow) 100%); }

  .closing-text { position: absolute; left: 560px; top: 670px; width: 465px; font-size: 12px; line-height: 15px; text-align: justify; color: var(--text); }
</style>
</head>
<body>
<main class="spread">

  <section class="goals-panel">
    <svg class="connectors" viewBox="0 0 528 600" aria-hidden="true">
      <g stroke="#1d1d1b" stroke-width="2" fill="none">
        <line x1="114" y1="159" x2="114" y2="208"/>
        <line x1="194" y1="386" x2="194" y2="437"/>
        <path d="M463 100 H496 Q506 100 506 110 V485 Q506 495 496 495 H468"/>
      </g>
      <g fill="#1d1d1b">
        <circle cx="114" cy="183" r="3.5"/>
        <circle cx="194" cy="411" r="3.5"/>
        <circle cx="506" cy="298" r="3.5"/>
      </g>
    </svg>

    <div class="goal-box box-child">
      <h3 class="goal-title">Pour L’enfant</h3>
      <ul class="goal-list">
        <li>Être fier de partager un moment de sa vie<br>scolaire, en toute simplicité, avec son parent.</li>
        <li>Développer son plein potentiel.</li>
        <li>Favoriser sa réussite éducative.</li>
      </ul>
    </div>

    <div class="goal-box box-school">
      <h3 class="goal-title">Pour L’école</h3>
      <ul class="goal-list">
        <li>Vivre un projet rassembleur.</li>
        <li>Valoriser le travail de l’équipe- école.</li>
        <li>Rayonner dans sa communauté.</li>
      </ul>
      <h3 class="goal-title">Pour L’enseignant</h3>
      <ul class="goal-list">
        <li>Encourager la réussite de ses élèves.</li>
        <li>Multiplier les moments privilégiés<br>parent-enfant-enseignant dans le milieu scolaire.</li>
      </ul>
    </div>

    <div class="goal-box box-parent">
      <h3 class="goal-title">Pour Le Parent</h3>
      <ul class="goal-list">
        <li>Développer un sentiment d’appartenance<br>envers l’école.</li>
        <li>Découvrir son enfant en tant qu’élève.</li>
        <li>Participer à la réussite et à la persévérance<br>scolaire de son enfant.</li>
      </ul>
    </div>

    <div class="role-badge badge-child">
      <div class="role-photo" role="img" aria-label="Photo d’un jeune enfant lisant dans une bibliothèque scolaire">
        <span class="role-label">Enfant</span>
      </div>
    </div>
    <div class="role-badge badge-school">
      <div class="role-photo" role="img" aria-label="Photo d’une enseignante avec des élèves en classe">
        <span class="role-label">École<br>Enseignant(e)s</span>
      </div>
    </div>
    <div class="role-badge badge-parent">
      <div class="role-photo" role="img" aria-label="Photo de parents marchant avec leur enfant dans un champ au coucher du soleil">
        <span class="role-label">Parent</span>
      </div>
    </div>

    <div class="side-title">Les journées de la famille<br>de Ste-Ondine</div>
  </section>

  <section class="participation-note">
    <p>Pour chaque occasion reliée au projet « Les journées de la famille de Sainte-Ondine»* vous serez informés par l’enseignant(e) de votre enfant afin que vous puissiez y participer.</p>
    <p>*Surveillez les apparitions du logo sur les communications lors des Journées de la famille de Sainte-Ondine!</p>
  </section>

  <div class="cover-photo" role="img" aria-label="Photo d’une enseignante faisant du bricolage avec deux enfants dans une classe de maternelle"></div>
  <svg class="photo-curve" viewBox="0 0 530 80" preserveAspectRatio="none" aria-hidden="true">
    <path d="M0 70 Q265 -10 530 40 V80 H0 Z" fill="#ffffff"/>
  </svg>

  <div class="kid-drawing drawing-left-back" role="img" aria-label="Dessin d’enfant coloré d’une maison"></div>
  <div class="kid-drawing drawing-left" role="img" aria-label="Dessin d’enfant d’un paysage fleuri"></div>
  <div class="kid-drawing drawing-right" role="img" aria-label="Dessin d’enfant d’une famille sous un arbre et un soleil"></div>

  <div class="logo-disc"><span class="logo-name">Sainte-Ondine</span></div>
  <h1 class="event-title">Les journées de la famille<br>de Ste-Ondine</h1>

  <section class="intro-text">
    <p>L’école Sainte-Ondine souhaite ouvrir ses portes afin que vous puissiez partager avec votre enfant des moments de sa vie d’élève. Vous connaissez votre enfant sous plusieurs de ses facettes. Avec ce projet, vous pourrez maintenant le connaître en tant qu’élève œuvrant dans son milieu scolaire.</p>
    <p>Vous serez invités, à divers moments de l’année scolaire, à participer au quotidien de votre enfant, par exemple…</p>
  </section>

  <section class="occasion-row">
    <div class="occasion occasion-class">lors d’activités<br>spéciales en classe<br>(ex.: lecture, bricolage,<br>présentation de métiers, etc.)</div>
    <div class="occasion occasion-events">lors d’événements<br>(ex.: la rentrée, chorale de Noël,<br>fête foraine, etc.)</div>
    <div class="occasion occasion-outings">lors de sorties éducatives<br>et sportives<br>(ex.: patinage, bibliothèque,<br>cinéma, etc.)</div>
  </section>

  <p class="closing-text">De plus, vous aurez l’opportunité de venir passer une période dans la classe de votre enfant. Vous aurez ainsi le privilège de l’accompagner lors d’un moment d’apprentissage habituel.</p>

</main>
</body>
</html>
```